"Precision Solutions for Aerospace Industries" product catalog Brennicor

General Catalog Guidelines
Format: A4, in vertical or horizontal orientation.
Cover Page: Should include the company logo, slogan, and website address (e.g., www.brennicor-example.com).
Layout: Each page can feature 1, 2, or up to 3 products, ensuring clarity and readability.
Catalog Content
1. Title Page
Catalog Name: "Technical Consumables for Aerospace".
Company Logo: BrenniCor.
High-Quality Image: Related to the aerospace industry.
2. Table of Contents
List of sections with corresponding page numbers for easy navigation.
3. Introduction / Scope of Activities
Company Overview: Brief introduction to BrenniCor's operations.
Specialization: Emphasis on manufacturing spare parts and consumables for special processes such as thermal spraying, diffusion brazing, welding, etc.
Certifications: Company certifications (AS9100, military concession) and a list of major clients.
Mission: "Brennicor's mission is to meet the requirements of thermal spray and aviation industry customers by continuous improvement of employees' qualifications, machining of difficult-to-machine materials using modern and non-conventional manufacturing processes, and new implementations of technological processes using developed know-how."
Vision: "To be a recognizable brand in the thermal spray and aviation industry on the global market. Be not only associated with the manufacturing of parts under the customers' purchase orders but also with innovative solutions that will bring many benefits to the contractor."
4. Key Sections of the Catalog
Consumables for Special Processes

Test coupons, panels, samples, and other elements for thermal spraying, chemical processing, welding.
Machining of difficult-to-machine materials such as nickel and cobalt-based superalloys, titanium, and hardened steel.
Reusable silicone masking and other masking solutions.
Coupons Regeneration

Description of the coupon regeneration process and its benefits (material savings, cost reduction, environmental impact).
Metal Parts and PSP Prefabricates

Structural elements, e.g., honeycombs, repair parts for turbines, ready-made PSP elements.
Machining and Support Services

Wire EDM cutting – benefits and applications.
Coating evaluation laboratory and technological accessories.
Consultations on technological processes, preparation for QUALTEX certification.
Modern Aviation Materials

Ceramic composites (CMC), nickel and cobalt-based superalloys, and other aerospace materials.
Repair and R&D Services

Examples of research and development projects (e.g., repair of Varnel 53 airfoils).
Solutions for issues related to thermal spraying and process optimization.
Additional Information

Information on hybrid additive manufacturing.
Current company status and client list.
5. Last Page
Contact Information:
Production Site: Wiktora Grabca 12, 05-410 Otwock, Poland.
R&D Center: Brzozówka 318B, 36-014 Brzozówka, Poland.
Email address, phone number, and social media links.
"Nice to Have" Elements
Inspirational Images: Products in use, e.g., aerospace tests, industrial applications
Updates

Project details can be found at this link https://files.example-share.net/t-KmQ4rwzLxa

Target Market(s)

aviation industry, metallurgy

Industry/Entity Type

Font styles to use
Sans Serif

Colors
0054AA
0677BA
7BADD7
CADEEF
E8F1F8
F0912C
F2A743
F7CA91
FBE8D2
FDF5EE

Requirements
Must have
• 1. Cover Eye-catching graphics. Your company logo. A short, clear title (e.g. catalog name, season, offer). 2. Table of contents Particularly important in larger catalogs. Makes it easier to quickly find individual sections. 3. Introduction / Company information A short company mission or introduction (information at https://brennicor-example.com/about-us/) 4. Key categories and sections Division into easy-to-understand sections, e.g.: Products, Services. 5. Product pages; 8. Aesthetics and readability Use colors consistent with the brand's visual identification. Consistent fonts and text hierarchy (e.g. titles larger than descriptions). Well-placed elements on the page so as not to overwhelm the viewer.
Nice to have
• Lifestyle inspirations and photos Photos from the industry such as: airplanes, turbines, lathe machines, WEDEM.

```html
<!DOCTYPE html>
<html lang="en">
<head>
<meta charset="utf-8">
<title>Brennicor Catalog – Table of Contents</title>
<link href="https://fonts.googleapis.com/css2?family=Montserrat:wght@400;500;600;700&display=swap" rel="stylesheet">
<style>
  :root{
    --backdrop:#8a8a8a;
    --paper:#ffffff;
    --brand-blue:#2b50a1;
    --ink:#1a1a1a;
    --bar-grey:#8c8c90;
    --thumb-shadow:#8f8f93;
    --thumb-bg:#eeeff3;
    --banner-bg:#f0f0f2;
  }
  *{margin:0;padding:0;box-sizing:border-box}
  html,body{width:1200px;height:1126px;overflow:hidden;background:var(--backdrop);font-family:'Montserrat',sans-serif;color:var(--ink)}
  .spread{position:absolute;left:52px;top:180px;width:1096px;height:740px;background:var(--paper)}
  .gutter{position:absolute;left:515px;top:0;width:26px;height:100%;background:linear-gradient(90deg,rgba(0,0,0,0) 0%,rgba(0,0,0,.05) 100%)}
  .abs{position:absolute}
  .page-title{left:51px;top:47px;font-size:16.5px;font-weight:500;color:var(--brand-blue);white-space:nowrap}
  .rule{height:10px;background:repeating-linear-gradient(180deg,var(--brand-blue) 0 1px,transparent 1px 3px)}
  .section-title{font-size:16.8px;font-weight:700;color:var(--brand-blue);letter-spacing:.5px;white-space:nowrap}
  .item{position:absolute;width:470px;height:60px}
  .thumb{position:absolute;left:0;top:0;width:59px;height:57px;background:var(--thumb-bg);box-shadow:5px 5px 0 var(--thumb-shadow)}
  .item-title{position:absolute;left:75px;top:2px;font-size:10.4px;font-weight:600;color:var(--brand-blue);line-height:12.5px;white-space:nowrap}
  .item-desc{position:absolute;left:75px;top:20px;width:326px;font-size:7px;font-weight:500;line-height:9px}
  .item-desc.justify{text-align:justify}
  .progress{position:absolute;left:415px;top:3px;width:8.5px;height:53px;background:var(--bar-grey)}
  .progress::after{content:"";position:absolute;left:0;bottom:0;width:100%;height:11px;background:var(--brand-blue)}
  .brand{left:890px;top:42px;display:flex;align-items:center;gap:6px;font-size:19px;font-weight:700;color:var(--brand-blue);letter-spacing:.5px}
  .brand-square{width:14px;height:14px;background:var(--brand-blue)}
  .services{left:603px;top:573px;width:493px;height:112px;background:var(--banner-bg);overflow:hidden}
  .services-photo{position:absolute;left:0;top:0;width:100%;height:100%}
  .services-heading{position:absolute;left:238px;top:22px;font-size:18px;font-weight:600;color:var(--brand-blue);white-space:nowrap}
  .services-heading small{font-size:10px;font-weight:600}
  .services-desc{position:absolute;left:245px;top:50px;width:185px;font-size:7px;font-weight:500;line-height:9px;text-align:center}
</style>
</head>
<body>
<div class="spread">
  <div class="gutter"></div>

  <h1 class="abs page-title">TABLE OF CONTENTS</h1>
  <div class="abs rule" style="left:251px;top:51px;width:246px"></div>
  <h2 class="abs section-title" style="left:51px;top:92px">CONSUMABLES FOR SPECIAL PROCESSES</h2>

  <div class="item" style="left:63px;top:132px">
    <div class="thumb" role="img" aria-label="Machined test coupon and small substrate plates" style="background:linear-gradient(135deg,#f1f2f5,#cfd1d6)"></div>
    <h3 class="item-title">Coupons &amp; Substrates Machining</h3>
    <p class="item-desc">We specialize in manufacturing high-quality test coupons, substrates, specimens, samples, button panels, discs, and strips for thermal spray, cold spray, chemical processing &amp; welding applications in the aviation industry. Our range of materials includes nickel and cobalt-based superalloys, titanium, hardened steel, and aluminum alloys.</p>
    <div class="progress"></div>
  </div>

  <div class="item" style="left:63px;top:214px">
    <div class="thumb" role="img" aria-label="Green silicone masking ring" style="background:radial-gradient(ellipse at 45% 55%,#f3f4f6 22%,#4c8a2e 26%,#2f5a1c 42%,#6b6457 52%,#eeeff3 60%)"></div>
    <h3 class="item-title">Reusable Silicone Masking / Hard Masking</h3>
    <p class="item-desc">Brennicor's reusable silicone masking improves productivity and reduces costs by providing precise, durable protection for aero and gas turbine engine parts during processes such as thermal spray, grit blasting, shot peening, chemical processing, and vibratory finishing</p>
    <div class="progress"></div>
  </div>

  <div class="item" style="left:63px;top:296px">
    <div class="thumb" role="img" aria-label="Dark metal block and disc spare parts" style="background:linear-gradient(160deg,#f1f2f5 40%,#5a5b60 60%,#e9eaee 80%)"></div>
    <h3 class="item-title">Fan Blade Leading Edge Patches, Custom Spare Metal Parts</h3>
    <p class="item-desc">Manufacturer of aerospace components and spare parts for turbine engines, offering a wide range of materials.</p>
    <div class="progress"></div>
  </div>

  <div class="item" style="left:63px;top:377px">
    <div class="thumb" role="img" aria-label="Two thin metal welding shims" style="background:linear-gradient(160deg,#f1f2f5 45%,#6b6458 52%,#f1f2f5 58%)"></div>
    <h3 class="item-title">Honeycomb Tack Welding Shims</h3>
    <p class="item-desc">Our shims are precision-made with flat surfaces, eliminating issues like convex edges that cause scorching on contact points and honeycomb surfaces. They ensure reliable performance and solve problems related to improper shim contact in demanding applications.</p>
    <div class="progress"></div>
  </div>

  <div class="item" style="left:63px;top:459px">
    <div class="thumb" role="img" aria-label="Slotted brazing preform strip" style="background:linear-gradient(135deg,#f1f2f5 35%,#d8b07c 50%,#f1f2f5 70%)"></div>
    <h3 class="item-title">Pre-Sintered Diffusion Brazing Preforms (PSP)</h3>
    <p class="item-desc">Superalloy and brazing products for aero engines, ideal for high-temperature repairs and dimensional restoration, with low porosity minimal shrinkage.</p>
    <div class="progress"></div>
  </div>

  <div class="item" style="left:63px;top:541px">
    <div class="thumb" role="img" aria-label="Dark grey honeycomb disc" style="background:radial-gradient(ellipse at 50% 50%,#4a4b50 45%,#eeeff3 55%)"></div>
    <h3 class="item-title">Honeycomb</h3>
    <p class="item-desc">Honeycomb structures, with or without embedded brazing material, tailored to customer specifications and available in various forms like segments and rings, offer reduced assembly time with tape application, while Brennicor also provides additional surface treatments as a value-added service.</p>
    <div class="progress"></div>
  </div>

  <div class="item" style="left:63px;top:622px">
    <div class="thumb" role="img" aria-label="Fanned set of feeler gauges" style="background:linear-gradient(150deg,#f1f2f5 30%,#9a9ca2 55%,#e3e4e8 75%)"></div>
    <h3 class="item-title">Custom Feeler Gauges Manufacturing</h3>
    <p class="item-desc">Thanks to our WEDM capabilities, we manufacture precise tooling for measuring thickness, gaps, and spacing such as the 0.1 mm feeler gauge shown in the photo.</p>
    <div class="progress"></div>
  </div>

  <div class="abs rule" style="left:596px;top:51px;width:254px"></div>
  <div class="abs brand"><span class="brand-square"></span>BRENNICOR</div>

  <div class="item" style="left:604px;top:88px">
    <div class="thumb" role="img" aria-label="Regenerated test coupon and plates" style="background:linear-gradient(135deg,#f1f2f5,#cfd1d6)"></div>
    <h3 class="item-title">Coupons regeneration</h3>
    <p class="item-desc justify">Our regeneration service restores coated coupons to their original specifications. By using mechanical stripping processes, we offer a faster and more cost-effective alternative to producing new coupons. This results in significant savings on raw materials and heat treatment, while also reducing waste.</p>
    <div class="progress"></div>
  </div>

  <h2 class="abs section-title" style="left:606px;top:181px">CONSUMABLES FOR AEROSPACE LABS</h2>

  <div class="item" style="left:604px;top:215px">
    <div class="thumb" role="img" aria-label="High-temperature metal accessory ring" style="background:radial-gradient(ellipse at 45% 55%,#f3f4f6 22%,#4c8a2e 26%,#2f5a1c 42%,#6b6457 52%,#eeeff3 60%)"></div>
    <h3 class="item-title">High-temperature Custom Metal Accessories</h3>
    <p class="item-desc">Custom accessories and high-temperature equipment: such as pull rods, couplings, fixtures, made of KRM K246/247 or other cast nickel superalloys, for creep, stress rupture and tensile testing at elevated temperatures up to 1300° C</p>
    <div class="progress"></div>
  </div>

  <div class="item" style="left:604px;top:282px">
    <div class="thumb" role="img" aria-label="Laboratory fixture block and disc" style="background:linear-gradient(160deg,#f1f2f5 40%,#5a5b60 60%,#e9eaee 80%)"></div>
    <h3 class="item-title">Coating Evaluation Laboratory Accessories</h3>
    <p class="item-desc">Manufacturing of custom laboratory accessories including, Gravity or pressure type V-grooved curing fixture for Tensile Bond Strength test of coating, Loading fixtures, concentricity gauge with dial indicator and more...</p>
    <div class="progress"></div>
  </div>

  <h2 class="abs section-title" style="left:606px;top:379px">MODERN AVIATION MATERIALS</h2>

  <div class="item" style="left:604px;top:410px">
    <div class="thumb" role="img" aria-label="Ceramic composite test specimen" style="background:linear-gradient(135deg,#f1f2f5,#cfd1d6)"></div>
    <h3 class="item-title">Ceramic Composites (Sic-SiC CMC)</h3>
    <p class="item-desc">Brennicor supplies CMC SiC-SiC materials and components for aerospace and R&amp;D driven by the growing use of CMCs in high-temperature engine parts.</p>
    <div class="progress"></div>
  </div>

  <div class="item" style="left:604px;top:481px">
    <div class="thumb" role="img" aria-label="Stack of metal alloy sheets" style="background:linear-gradient(150deg,#9c9ea3 10%,#e9eaec 40%,#4b4c50 70%,#b5b7bb 100%)"></div>
    <h3 class="item-title">Aerospace Nickel &amp; Cobalt Base Superalloys,<br>Titanium, Steel, Aluminum Alloys</h3>
    <p class="item-desc" style="top:34px">Brennicor offers a comprehensive range of aerospace raw materials (wrought and cast). Including Inverel Varnel, KRM, GLD, PXA, CXN (Single Crystals), Haltrin and many others. We are able to supply difficult to find raw materials in required shapes and dimensions.</p>
    <div class="progress" style="top:6px"></div>
  </div>

  <section class="abs services">
    <svg class="services-photo" viewBox="0 0 493 112" preserveAspectRatio="none" role="img" aria-label="Wire EDM machine cutting head in close-up">
      <defs>
        <linearGradient id="wedm" x1="0" y1="0" x2="1" y2="1">
          <stop offset="0" stop-color="#6d7076"/>
          <stop offset=".45" stop-color="#c9cbcf"/>
          <stop offset="1" stop-color="#3f4146"/>
        </linearGradient>
      </defs>
      <polygon points="0,0 189,0 287,112 0,112" fill="url(#wedm)"/>
    </svg>
    <h2 class="services-heading">SERVICES <small>WIRE EDM (WEDM)</small></h2>
    <p class="services-desc">Our advanced WEDM technology allows cutting materials up to 700mm thick ensuring minimal thermal impact and the highest precision</p>
  </section>
</div>
</body>
</html>
```